Used Truck and Machinery dealer needs a new website

We require a new website four our business which is in the early stages of becoming fully online. We have been a truck and machinery dealer in Western Australia since 1974. We have had many tries at websites over the years, but have never been too pleased with the result (mainly because I have tried doing it myself, rather than a professional). Currently, we run an Pagelofty site as a stop gap (seen at www.haulerandrig.com.au) which a super awesome design company threw together for us, but we need to iframe (shudder) our stock into the page from a third party inventory site (This will change most likely to the motorbin dealer network in the near future, which uses a script to integrate) (Direct link to the stock on the current site: https://www.rigmarket.com.au/search/hauler-(and)-rig/all-for-sale/?query=v~1-z~15-) I want the page to be responsive (knowing full well having an iframe makes this difficult, so interested to see what can be done there), Most of the clientele prefer to phone, so having a layout similar to what you can see on our Ppagelofty works (i.e. our number to be seen as soon as you are on page), also have a request callback feature (e.g. contact form). We also need a second contact form to be added for Valuations. In a nutshell, we value all types of vehicles, including trailers and machines to ensure that the client is paying the correct insurance premium, plus we value equipment for 99% of Australia's insurance companies when a dispute is made regarding the true value of the item. I would like a google map embedded to find our premises. I want the site to be SEO'd. I like the current design but would like it to be more colour neutral, but tying in with our company logo. Ideally, I want to use a popular CMS such as Wordpress or Drupal but open to others if you feel there is a better option.
I have mentioned 3 pages, on the main page is to have about us with the following text:
"Corrabee Hauler and Rig have been a specialist in heavy trucks and machinery for over 35 years. We source equipment on request, consign vehicles and have a steady flow of new stock arriving weekly.

We have been operating as a licensed valuer for vehicles large and small for a number of years and are contracted to 99% of Australia’s insurance companies to value pre accident vehicles.

We also conduct full fleet valuations to help you keep your premiums at a realistic figure."

It should have our contact details, plus our address.

The second page should have our stock listed and integrated with https://www.rigmarket.com.au/search/hauler-(and)-rig/all-for-sale/?query=v~1-z~15-

The Third page should be a contact page with the usual contact form but also have an evaluation form also with the following fields:
Name, Email, Phone, Location of Item(s), Make, Model, Year, Registration Number, Condition (Drop down with Excellent | Fair | Poor) and, Additional Comments

It should have social icons to Plain circle and Plain circle:
Plain circle Link: http://facebook.com/corrabeehaulers
Plain circle Link: https://www.instagram.com/haulerandrigcorrabee/

I have uploaded some of our artwork to assist.Finally, we have our own hosting with HostNubo which includes:15GB High-Speed SSD Storage Unlimited Premium Bandwidth Unlimited Addon & Parked Domains Unlimited MariaDB Databases 200% CPU Allowance 4GB Memory Allowance Hourly Varkelo Backups FREE Tessime SSL Certificates I will give the winning designer access to the hosting platform to upload the final design and have it live at www.haulerandrig.com.auI will require an overview of the site on how to maintain moving forward. Thank you

Target Market(s)

People wishing to purchase a used heavy vehicle such as a Truck, Trailer or Machine

Industry/Entity Type

Automotive

Coding

Coded - Design and coding required

Number of Pages Required

3 page

Font styles to use
Serif
Sans Serif
Decorative
Script

Colors

Designer to choose colors to be used in the design.

Requirements
Must have
• Integration into the existing stock located at https://www.rigmarket.com.au/search/hauler-(and)-rig/all-for-sale/?query=v~1-z~15-)
• Must be on our hosting platform at HostNubo
• Must be as responsive as possible even though you will have to integrate with a third party site
• Must be on a popular CMS
• Must be SEO'd

```html
<!DOCTYPE html>
<html lang="en">
<head>
<meta charset="utf-8">
<title>Corrabee Hauler and Rig</title>
<link href="https://fonts.googleapis.com/css2?family=Poppins:wght@300;400;500;600;700&display=swap" rel="stylesheet">
<style>
:root{
  --red:#e8252c;
  --red-deep:#d01c26;
  --dark:#2b2b2b;
  --ink:#333;
  --muted:#777;
  --white:#fff;
  --line:#d9d9d9;
}
*{box-sizing:border-box;margin:0;padding:0}
html,body{width:1200px;height:3377px;overflow:hidden}
body{font-family:"Poppins",sans-serif;color:var(--ink);background:var(--white);position:relative}
a{color:inherit;text-decoration:none}

/* Hero */
.hero{position:relative;height:687px;color:var(--white)}
.hero-photo{position:absolute;inset:0;background:linear-gradient(180deg,#6d6a66 0%,#8a7561 45%,#b58a62 75%,#c69a6e 100%)}
.hero-shade{position:absolute;inset:0;background:linear-gradient(180deg,rgba(0,0,0,.45) 0%,rgba(0,0,0,.15) 30%,rgba(0,0,0,.1) 100%)}
.topbar{position:absolute;top:0;left:0;right:0;height:45px;display:flex;align-items:center;font-size:14px;padding:0 110px}
.topbar .item{display:flex;align-items:center;gap:6px;margin-right:28px}
.topbar .phone{margin-left:auto;font-size:17px}
.topbar .lang{margin-left:32px}
.navbar{position:absolute;top:62px;left:130px;right:92px;display:flex;align-items:center}
.brand{display:flex;align-items:center;gap:10px;font-weight:700;font-size:28px;letter-spacing:.5px}
.brand-dot{width:34px;height:34px;border-radius:50%;background:var(--red)}
.menu{margin-left:auto;display:flex;gap:34px;font-size:16px}
.menu .active{color:var(--red)}
.hero-copy{position:absolute;top:288px;left:0;right:0;text-align:center}
.hero-title{font-size:44px;font-weight:600;letter-spacing:.5px;text-transform:uppercase}
.hero-sub{font-size:21px;font-weight:500;margin-top:12px;text-transform:uppercase}
.btn{display:inline-flex;align-items:center;justify-content:center;background:var(--red);color:var(--white);font-weight:600;border-radius:30px}
.hero-cta{margin-top:22px;width:226px;height:50px;font-size:17px}
.follow{position:absolute;left:66px;top:280px;display:flex;flex-direction:column;align-items:center;gap:18px;font-size:12px}
.follow .s{width:12px;height:12px;border-radius:50%;border:2px solid var(--white)}
.follow .label{writing-mode:vertical-rl;transform:rotate(180deg);margin-top:20px}
.dots{position:absolute;right:60px;top:336px;display:flex;flex-direction:column;align-items:center;gap:20px}
.dots span{width:10px;height:10px;border-radius:50%;background:var(--white)}
.dots .on{width:22px;height:22px;background:none;border:3px solid var(--white);position:relative}
.dots .on::after{content:"";position:absolute;inset:3px;border-radius:50%;background:var(--white)}

/* Evaluation */
.evaluation{height:342px;text-align:center;padding-top:44px}
.section-title{color:var(--red);font-size:25px;font-weight:700;text-transform:uppercase}
.evaluation .lead{font-size:15px;margin-top:14px;color:var(--ink)}
.eval-grid{display:grid;grid-template-columns:repeat(4,218px);gap:20px 23px;width:941px;margin:26px auto 0}
.field{height:38px;border:1px solid var(--line);box-shadow:0 1px 3px rgba(0,0,0,.12);display:flex;align-items:center;justify-content:space-between;padding:0 14px;font-size:12px;color:#555}
.field .caret{width:0;height:0;border-left:5px solid transparent;border-right:5px solid transparent;border-top:7px solid var(--red)}
.eval-btn{margin-top:22px;width:214px;height:36px;font-size:13px;border-radius:0}

/* About */
.about{height:434px;background:var(--red);color:var(--white);position:relative}
.about-copy{position:absolute;left:110px;top:55px;width:480px}
.about-copy h2{font-size:31px;font-weight:700}
.about-copy p{font-size:13px;line-height:29px;margin-top:8px}
.about-copy p+p{margin-top:0}
.about-actions{display:flex;gap:18px;margin-top:12px}
.btn-light{background:var(--white);color:var(--red);height:46px;font-size:15px}
.collage{position:absolute}
.c1{left:768px;top:30px;width:302px;height:162px;background:linear-gradient(160deg,#8a8f94,#7a5b3b 60%,#9a6a42)}
.c2{left:651px;top:191px;width:184px;height:223px;background:linear-gradient(170deg,#c8d3d8,#c28a58 55%,#b06c3a)}
.c3{left:834px;top:156px;width:319px;height:258px;background:linear-gradient(175deg,#d8dde0 0%,#c7b79c 40%,#b3744a 75%,#9a5630 100%);border:4px solid var(--red)}

/* Trucks */
.trucks{height:541px;position:relative}
.trucks-head{position:absolute;top:31px;left:97px;right:90px;height:44px;display:flex;align-items:center}
.refine{width:205px;height:44px;font-size:16px;gap:8px}
.trucks-head .section-title{position:absolute;left:0;right:0;text-align:center;pointer-events:none;font-size:25px}
.tools{margin-left:auto;display:flex;gap:16px;color:var(--red);font-size:16px;font-weight:500}
.tools span{display:flex;align-items:center;gap:6px}
.listing-photo{position:absolute;left:97px;top:117px;width:448px;height:248px;background:linear-gradient(180deg,#8d939a,#3d4a7a 55%,#2c2f3a)}
.thumb{position:absolute;top:374px;width:142px;height:126px}
.t1{left:97px;background:linear-gradient(180deg,#6f7f98,#3a4e8a)}
.t2{left:250px;background:linear-gradient(180deg,#9a9a94,#5d5f6a)}
.t3{left:403px;background:linear-gradient(180deg,#4d5a8c,#2c3568)}
.arrow{position:absolute;top:290px;color:var(--red)}
.arrow.l{left:58px}.arrow.r{right:58px}
.listing{position:absolute;left:585px;top:138px;width:530px}
.listing h3{color:var(--red);font-size:26px;font-weight:600}
.meta{display:flex;gap:22px;font-size:16px;margin-top:14px}
.meta span{display:flex;align-items:center;gap:6px}
.disclaimer{font-size:15px;line-height:28px;margin-top:14px}
.disclaimer em{color:var(--red);font-style:normal}
.price{font-size:27px;font-weight:700;margin-top:22px}
.price small{font-size:14px;font-weight:600}
.gst{font-size:14px;font-weight:600;margin-top:4px}
.listing-actions{display:flex;gap:10px;margin-top:22px}
.listing-actions .btn{height:50px;width:158px;font-size:17px}
.listing-actions .btn+.btn{width:160px}

/* Services */
.services{height:327px;background:linear-gradient(180deg,var(--red) 0%,#e4343a 100%);color:var(--white);text-align:center;padding-top:44px;border-top:4px solid #eee}
.services h2{font-size:31px;font-weight:700}
.service-row{display:flex;justify-content:center;gap:50px;margin-top:22px}
.service{width:300px}
.service svg{height:72px}
.service h4{font-size:25px;font-weight:500;margin-top:4px}
.service p{font-size:15px;line-height:28px;opacity:.9;margin-top:6px}

/* Map */
.map{height:324px;position:relative;background:linear-gradient(120deg,#b9dff0 0%,#e9e7dd 30%,#cfe6c3 60%,#b8d9a4 100%)}
.map-card{position:absolute;left:99px;top:85px;width:284px;height:162px;background:var(--white);box-shadow:0 2px 8px rgba(0,0,0,.25);padding:18px 34px;font-size:13px;line-height:25px}
.map-pin{position:absolute;left:416px;top:88px}

/* Contact */
.contact{height:628px;display:flex}
.contact-form{width:628px;background:var(--red-deep);color:var(--white);padding:76px 0 0 122px}
.contact-form h2,.contact-info h2{font-size:29px;font-weight:700}
.cf-field{width:446px;border-bottom:2px solid rgba(255,255,255,.85);height:44px;display:flex;align-items:flex-end;gap:10px;padding:0 0 8px 8px;font-size:16px;margin-top:26px}
.cf-field:first-of-type{margin-top:30px}
.cf-message{width:446px;border-bottom:2px solid rgba(255,255,255,.85);height:84px;font-size:16px;padding:4px 0 0 8px;margin-top:22px}
.submit{margin-top:30px;width:226px;height:52px;background:#111;color:var(--white);display:flex;align-items:center;justify-content:center;font-size:20px;font-weight:600}
.contact-info{flex:1;background:linear-gradient(135deg,#3a3a3a 0%,#2a2a2a 50%,#4a4a4a 100%);color:var(--white);padding:76px 0 0 66px}
.ci-label{display:flex;align-items:center;gap:10px;font-size:19px;font-weight:600;margin-top:34px}
.ci-label:first-of-type{margin-top:44px}
.ci-value{font-size:20px;margin-top:4px;padding-left:2px}
.socials{display:flex;gap:16px;margin-top:12px}
.socials span{width:46px;height:46px;border-radius:50%;border:2px solid var(--white)}

/* Footer */
.footer{height:90px;display:flex;align-items:center;justify-content:center;font-size:15px;color:#8a8a8a}
</style>
</head>
<body>

<header class="hero">
  <div class="hero-photo" role="img" aria-label="Road trains with oversize loads on an outback highway"></div>
  <div class="hero-shade"></div>
  <div class="topbar">
    <span class="item"><svg width="12" height="14" viewBox="0 0 12 14"><path d="M6 0a5 5 0 0 1 5 5c0 4-5 9-5 9S1 9 1 5a5 5 0 0 1 5-5z" fill="#e8252c"/><circle cx="6" cy="5" r="2" fill="#fff"/></svg>42 Corrabee Road, Corrabee, WA 6190</span>
    <span class="item"><svg width="14" height="10" viewBox="0 0 14 10"><rect width="14" height="10" rx="1" fill="#e8252c"/><path d="M0 1l7 5 7-5" stroke="#fff" fill="none"/></svg>info@haulerandrig.com.au</span>
    <span class="item phone"><svg width="14" height="14" viewBox="0 0 14 14"><path d="M3 1l2 3-1.5 1.5a8 8 0 0 0 5 5L10 9l3 2-1 2.5C6 13 1 8 .5 2z" fill="#e8252c"/></svg>08 9471 5830</span>
    <span class="lang">English ▾</span>
  </div>
  <nav class="navbar">
    <a class="brand" href="#"><span class="brand-dot"></span>HAULER&amp;RIG</a>
    <div class="menu">
      <a class="active" href="#">Home</a><a href="#">About Us</a><a href="#">Get An Evaluation</a><a href="#">Find Trucks for Sale</a><a href="#">Contact</a>
    </div>
  </nav>
  <div class="follow"><span class="s"></span><span class="s"></span><span class="label">Follow Us</span></div>
  <div class="hero-copy">
    <h1 class="hero-title">Corrabee Hauler and Rig</h1>
    <p class="hero-sub">Truck specialist for over 35 years</p>
    <a class="btn hero-cta" href="#">REQUEST CALL BACK</a>
  </div>
  <div class="dots"><span></span><span class="on"></span><span></span></div>
</header>

<section class="evaluation">
  <h2 class="section-title">Get your truck or fleet evaluated from the experts</h2>
  <p class="lead">We conduct full fleet valuations to help you keep your premiums at a realistic figure.</p>
  <div class="eval-grid">
    <div class="field">Name</div>
    <div class="field">Email</div>
    <div class="field">Suburb of Item</div>
    <div class="field">Make<span class="caret"></span></div>
    <div class="field">Model<span class="caret"></span></div>
    <div class="field">Year<span class="caret"></span></div>
    <div class="field">Registration<span class="caret"></span></div>
    <div class="field">Condition<span class="caret"></span></div>
  </div>
  <a class="btn eval-btn" href="#">GET YOUR EVALUATION</a>
</section>

<section class="about">
  <div class="about-copy">
    <h2>ABOUT US</h2>
    <p>Corrabee Hauler and Rig have been a specialist in heavy trucks and machinery for over 35 years. We source equipment on request, consign vehicles and have a steady flow of new stock arriving weekly.</p>
    <p>We have been operating as a licensed valuer for vehicles large and small for a number of years and are contracted to 99% of Australia's insurance companies to value pre accident vehicles.</p>
    <p>We also conduct full fleet valuations to help you keep your premiums at a realistic figure.</p>
    <div class="about-actions">
      <a class="btn btn-light" style="width:190px" href="#">Find Trucks for Sale</a>
      <a class="btn btn-light" style="width:137px" href="#">Get a Quote</a>
    </div>
  </div>
  <div class="collage c1" role="img" aria-label="Heavy truck parked in the yard"></div>
  <div class="collage c2" role="img" aria-label="Earthmoving machine on red dirt"></div>
  <div class="collage c3" role="img" aria-label="Low loader carrying machinery in the outback"></div>
</section>

<section class="trucks">
  <div class="trucks-head">
    <a class="btn refine" href="#">Refine search <svg width="16" height="16" viewBox="0 0 16 16"><circle cx="6.5" cy="6.5" r="5" stroke="#fff" stroke-width="2.2" fill="none"/><path d="M10 10l5 5" stroke="#fff" stroke-width="2.4"/></svg></a>
    <h2 class="section-title">Trucks</h2>
    <div class="tools">
      <span><svg width="16" height="14" viewBox="0 0 16 14"><path d="M0 2h16M3 7h10M6 12h4" stroke="#e8252c" stroke-width="2"/></svg>Filter</span>
      <span><svg width="15" height="15" viewBox="0 0 15 15" fill="#e8252c"><rect width="4" height="4"/><rect x="5.5" width="4" height="4"/><rect x="11" width="4" height="4"/><rect y="5.5" width="4" height="4"/><rect x="5.5" y="5.5" width="4" height="4"/><rect x="11" y="5.5" width="4" height="4"/><rect y="11" width="4" height="4"/><rect x="5.5" y="11" width="4" height="4"/><rect x="11" y="11" width="4" height="4"/></svg>Change layout</span>
    </div>
  </div>
  <svg class="arrow l" width="20" height="32" viewBox="0 0 20 32"><path d="M17 2L4 16l13 14" stroke="#e8252c" stroke-width="4" fill="none"/></svg>
  <svg class="arrow r" width="20" height="32" viewBox="0 0 20 32"><path d="M3 2l13 14L3 30" stroke="#e8252c" stroke-width="4" fill="none"/></svg>
  <div class="listing-photo" role="img" aria-label="Blue dolly trailer wheels behind a wire fence"></div>
  <div class="thumb t1" role="img" aria-label="Dolly trailer side view"></div>
  <div class="thumb t2" role="img" aria-label="Dolly trailer rear view"></div>
  <div class="thumb t3" role="img" aria-label="Dolly trailer close up"></div>
  <div class="listing">
    <h3>2017 Unknown Dolly Dollys</h3>
    <div class="meta">
      <span><svg width="18" height="18" viewBox="0 0 18 18"><path d="M2 16L16 2M5 9l4 4M9 5l4 4" stroke="#e8252c" stroke-width="2"/></svg>Airbag</span>
      <span><svg width="12" height="16" viewBox="0 0 12 16"><path d="M6 0a6 6 0 0 1 6 6c0 4.5-6 10-6 10S0 10.5 0 6a6 6 0 0 1 6-6z" fill="#e8252c"/><circle cx="6" cy="6" r="2.2" fill="#fff"/></svg>42 Corrabee Road, Corrabee WA 6190</span>
    </div>
    <p class="disclaimer"><em>Disclaimer:</em> Check with the seller to confirm vehicle details &amp; if any additional fees or charges apply. The information contained on this site is to be used as a guide only.</p>
    <p class="price">$27,500 <small>AUD</small></p>
    <p class="gst">Includes GST</p>
    <div class="listing-actions"><a class="btn" href="#">More Details</a><a class="btn" href="#">Get Finance</a></div>
  </div>
</section>

<section class="services">
  <h2>WHAT WE DO</h2>
  <div class="service-row">
    <div class="service">
      <svg width="72" height="72" viewBox="0 0 72 72" fill="none" stroke="#fff" stroke-width="2.5"><circle cx="38" cy="16" r="12"/><path d="M38 9v14M34 12h6a2.5 2.5 0 0 1 0 5h-4a2.5 2.5 0 0 0 0 5h6"/><path d="M6 50l14-8h14l8 4h-14M6 64l10-6h20l22-14-4-4-16 8"/></svg>
      <h4>Truck Finance</h4>
      <p>Fusce sollicitudin lorem et luctus volutpat. Proin placerat dapibus gravida.</p>
    </div>
    <div class="service">
      <svg width="90" height="72" viewBox="0 0 90 72" fill="none" stroke="#fff" stroke-width="2.5"><rect x="4" y="10" width="52" height="40"/><path d="M56 22h16l12 14v14H56z"/><circle cx="20" cy="56" r="7"/><circle cx="70" cy="56" r="7"/><path d="M14 24h30M14 34h22"/></svg>
      <h4>Dealer Benefits</h4>
      <p>Fusce sollicitudin lorem et luctus volutpat. Proin placerat dapibus gravida.</p>
    </div>
    <div class="service">
      <svg width="72" height="72" viewBox="0 0 72 72" fill="none" stroke="#fff" stroke-width="2.5"><rect x="12" y="4" width="42" height="60"/><path d="M20 16h26M20 26h26M20 36h18M20 46h14"/><path d="M58 20v40l-4 6-4-6V20z"/></svg>
      <h4>Easy Paperworks</h4>
      <p>Fusce sollicitudin lorem et luctus volutpat. Proin placerat dapibus gravida.</p>
    </div>
  </div>
</section>

<section class="map" role="img" aria-label="Street map showing the yard location in Corrabee">
  <svg class="map-pin" width="24" height="34" viewBox="0 0 24 34"><path d="M12 0a12 12 0 0 1 12 12c0 9-12 22-12 22S0 21 0 12A12 12 0 0 1 12 0z" fill="#e8252c"/><circle cx="12" cy="12" r="4" fill="#7a1010"/></svg>
  <div class="map-card">
    42 Corrabee Road, Corrabee,<br>WA 6190<br>08 9471 5830<br>info@haulerandrig.com.au<br>Mon. - Sun: 09:00 - 19:00
  </div>
</section>

<section class="contact">
  <div class="contact-form">
    <h2>CONTACT US FORM</h2>
    <div class="cf-field"><svg width="16" height="16" viewBox="0 0 16 16" fill="#fff"><circle cx="8" cy="5" r="4"/><path d="M0 16c0-5 4-7 8-7s8 2 8 7z"/></svg>NAME</div>
    <div class="cf-field"><svg width="16" height="12" viewBox="0 0 16 12"><rect width="16" height="12" fill="#fff"/><path d="M0 1l8 6 8-6" stroke="#d01c26" fill="none" stroke-width="1.5"/></svg>EMAIL</div>
    <div class="cf-field"><svg width="16" height="16" viewBox="0 0 14 14"><path d="M3 1l2 3-1.5 1.5a8 8 0 0 0 5 5L10 9l3 2-1 2.5C6 13 1 8 .5 2z" fill="#fff"/></svg>PHONE</div>
    <div class="cf-message">MESSAGE</div>
    <a class="submit" href="#">GET IN TOUCH</a>
  </div>
  <div class="contact-info" role="img" aria-label="Truck cab photographed in low light">
    <h2>CONTACT INFO</h2>
    <div class="ci-label"><svg width="14" height="18" viewBox="0 0 12 16"><path d="M6 0a6 6 0 0 1 6 6c0 4.5-6 10-6 10S0 10.5 0 6a6 6 0 0 1 6-6z" fill="#fff"/><circle cx="6" cy="6" r="2.2" fill="#333"/></svg>ADDRESS</div>
    <div class="ci-value">42 Corrabee Road, Corrabee, WA 6190</div>
    <div class="ci-label"><svg width="16" height="16" viewBox="0 0 14 14"><path d="M3 1l2 3-1.5 1.5a8 8 0 0 0 5 5L10 9l3 2-1 2.5C6 13 1 8 .5 2z" fill="#fff"/></svg>PHONE NUMBER</div>
    <div class="ci-value">08 9471 5830</div>
    <div class="ci-label">FOLLOW US</div>
    <div class="socials"><span aria-label="Social profile one"></span><span aria-label="Social profile two"></span></div>
  </div>
</section>

<footer class="footer">© 2018 Company Name &nbsp;All right reserved &nbsp;Term of Use</footer>

</body>
</html>
```